Business Card Design Project

We are a distribution company providing goods to Latin America. We sell everything from Medical equipment, generic medicines, to carecliners. The logo that we use is attached. The logo can incorporate different colors other than black for versatility. The company name is Valdoria International Corporation and/or VIC. The card will be printed using 1 or more of the following: Silk mounted and/or embossed. So if the design ideas could be made to incorporate that technique or any other unique techniques, it would be great. The target market is dialysis centers/doctors.

Basic Info for card:
Marnie Dowsett
Purchasing Manager
555-317-4086 direct
555-241-7953 fax
marnie.dowsett@valdoriavic.example
www.valdoriavic.example

Target Market(s)

Latin America

Industry/Entity Type

Business

Requirements
Nice to have
• The Front of the card should have the basic contact information with company name/logo. The back of the card could incorporate

```html
<!DOCTYPE html>
<html lang="en">
<head>
<meta charset="utf-8">
<title>Valdoria International Corporation – Business Card</title>
<link rel="stylesheet" href="https://fonts.googleapis.com/css2?family=Oswald:wght@300;400&family=Open+Sans:wght@400&display=swap">
<style>
  :root {
    --backdrop-light: #d4d4d4;
    --backdrop-dark: #9a9a9a;
    --brand-green: #1f4a22;
    --brand-green-deep: #0d1f0f;
    --ink-dark: #1b1b1b;
    --ink-mid: #333333;
    --paper: #ffffff;
    --label-ink: #1e1e1e;
  }
  html, body {
    margin: 0;
    padding: 0;
    overflow: hidden;
  }
  body {
    width: 872px;
    height: 1200px;
    position: relative;
    background: radial-gradient(ellipse at 50% 45%, var(--backdrop-light) 0%, #bdbdbd 60%, var(--backdrop-dark) 100%);
    font-family: "Oswald", sans-serif;
  }
  .card {
    position: absolute;
    left: 78px;
    width: 730px;
    background: var(--paper);
    box-shadow: 0 6px 18px rgba(0,0,0,0.35);
    overflow: hidden;
  }
  .card--front { top: 78px; height: 522px; }
  .card--back { top: 675px; height: 385px; }

  .front-band {
    position: absolute;
    left: 0; top: 0;
    width: 100%; height: 235px;
    background: radial-gradient(ellipse at 60% 40%, var(--brand-green) 0%, #173a19 45%, var(--brand-green-deep) 100%);
  }
  .brand {
    position: absolute;
    display: flex;
    align-items: center;
    gap: 26px;
  }
  .brand__name {
    text-align: center;
    line-height: 1;
    text-transform: uppercase;
    font-weight: 400;
  }
  .brand__name span { display: block; }
  .brand__word-lead { font-size: 54px; letter-spacing: 2px; }
  .brand__word-mid { font-size: 31px; letter-spacing: 1px; margin-top: 4px; }
  .brand__word-tail { font-size: 40px; letter-spacing: 1px; margin-top: 4px; }
  .brand__mark {
    width: 120px; height: 120px;
    border-radius: 50%;
  }
  .brand--front { left: 130px; top: 46px; color: var(--paper); }
  .brand--front .brand__mark { background: var(--paper); opacity: 0.9; }
  .brand--back { left: 140px; top: 118px; color: var(--brand-green); }
  .brand--back .brand__mark { background: var(--brand-green); }

  .contact-lines {
    position: absolute;
    left: 34px; top: 262px;
    color: var(--ink-dark);
    font-weight: 300;
    font-size: 31px;
    line-height: 45px;
  }
  .contact-lines small { font-size: 21px; margin-left: 6px; }
  .person {
    position: absolute;
    right: 26px; top: 250px;
    text-align: right;
    color: var(--ink-dark);
  }
  .person__name { font-size: 42px; font-weight: 400; color: var(--brand-green); line-height: 1.15; }
  .person__title { font-size: 30px; font-weight: 300; line-height: 1.3; }
  .person__email { font-size: 22px; font-weight: 300; margin-top: 12px; }

  .address-strip {
    position: absolute;
    left: 0; bottom: 0;
    width: 100%; height: 52px;
    background: var(--brand-green-deep);
    border-top: 4px solid var(--brand-green);
    color: var(--paper);
    font-size: 20px;
    font-weight: 300;
    line-height: 48px;
    text-align: right;
    padding-right: 120px;
    box-sizing: border-box;
  }

  .card-label {
    position: absolute;
    left: 78px;
    font-family: "Open Sans", sans-serif;
    font-size: 38px;
    color: var(--label-ink);
    margin: 0;
  }
  .card-label--front { top: 608px; }
  .card-label--back { top: 1078px; }
</style>
</head>
<body>
  <section class="card card--front" aria-label="Front side of card">
    <div class="front-band"></div>
    <div class="brand brand--front">
      <div class="brand__name">
        <span class="brand__word-lead">Valdoria</span>
        <span class="brand__word-mid">International</span>
        <span class="brand__word-tail">Corporation</span>
      </div>
      <div class="brand__mark"></div>
    </div>
    <div class="contact-lines">
      <div>555-317-4086<small>direct</small></div>
      <div>555-241-7953<small>fax</small></div>
      <div>www.valdoriavic.example</div>
    </div>
    <div class="person">
      <div class="person__name">Marnie Dowsett</div>
      <div class="person__title">Purchasing Manager</div>
      <div class="person__email">marnie.dowsett@valdoriavic.example</div>
    </div>
    <div class="address-strip">4471 NW 8th Avenue Portvale, ZZ 00000</div>
  </section>
  <p class="card-label card-label--front">Front side of card</p>

  <section class="card card--back" aria-label="Back side of card">
    <div class="brand brand--back">
      <div class="brand__name">
        <span class="brand__word-lead">Valdoria</span>
        <span class="brand__word-mid">International</span>
        <span class="brand__word-tail">Corporation</span>
      </div>
      <div class="brand__mark"></div>
    </div>
  </section>
  <p class="card-label card-label--back">Back side of card</p>
</body>
</html>
```